TRU Staffing DL Flyer

Tru staffing needs a glossy brochure designed for an upcoming VIP event of our clients which are real estate agencies.

Background:
Tru Staffing specialises in Realestate recruitment in Australia. We have been in the Realestate Recruitment industry for 18 years and are the highest referred agency in the Brisbane Market. We Recruit Property Managers, Commercial and Residential, Sales and support staff for our clients.

Guideline:
- The flyer will be DL size (210x99mm)
- We would like to see designs that use the colors Green and Black same as our logo (attached)
- We would like something modern with a sleek corporate feel
- Need to include other information as detailed below in the "Must have" section
Updates

My logo and contact details is a must on the DHL flyer

Design is up to you

Kind Regards

Leon

Reason: Hi Designers Thank you for your help it is a very hard decision that is why I have made 1. prize $160 and 2. prize $100 and extended the deadline until Wednesday. Kind Regards Leon

Target Market(s)

Residential and Commercial Realestate firms in Australia

Industry/Entity Type

Real Estate

Requirements
Must have
• Why clients use TRU:
With extensive years of recruitment experience we are the highest referred recruitment company in the Brisbane market.“Our clients benefit from our wealth of experience and knowledge within their industry to recruit the right candidate.”

- Why Candidates use TRU:
“With our long standing experience within recruitment , we take the time and care attitude to find the right position and culture suityour working experience."

- Tru Logo
- Website details: www.trustaffing.com.au
- Contact details:
Leon Ashford
Recruitment Manager
Mb: 0412 583 216
Ph: 3715 2649
Fax: 3715 2687
E: leon@trustaffing.com.au
Level 1/ 142 Harlow Street, Fernvale QLD 4306
Nice to have
• - Why Tru does quality and background checks on candidates
- The advantage of using Tru Staffing vs Recruitment on your own
- 12 week Guarantee period on all placements

```html
<!DOCTYPE html>
<html lang="en">
<head>
<meta charset="utf-8">
<title>TRU Staffing DL Flyer</title>
<link rel="stylesheet" href="https://fonts.googleapis.com/css2?family=Arimo:ital,wght@0,400;0,700;1,700&display=swap">
<style>
:root{
  --green:#5cbb46;
  --black:#000000;
  --white:#ffffff;
  --paper:#f4f4f4;
  --ink:#111111;
  --page:#ffffff;
}
*{margin:0;padding:0;box-sizing:border-box}
html,body{width:1200px;height:848px;overflow:hidden;background:var(--page)}
body{position:relative;font-family:"Arimo",Arial,sans-serif;color:var(--ink)}

.flyer{position:absolute;width:298px;height:633px;background:var(--paper);box-shadow:3px 4px 6px rgba(0,0,0,.25);overflow:hidden}
.flyer--front{left:256px;top:57px}
.flyer--back{left:646px;top:158px}

.brand{position:absolute;left:27px;top:30px;height:88px;width:240px;display:flex;align-items:center;gap:10px}
.brand__dot{width:40px;height:40px;border-radius:50%;background:var(--green);flex:none}
.brand__name{font-weight:700;font-size:30px;color:var(--black);letter-spacing:-.5px;white-space:nowrap}

.panel{position:absolute;left:0;width:100%;background:var(--black);padding:0 27px}
.flyer--front .panel{top:144px;height:334px;padding-top:28px}
.flyer--back .panel{top:144px;height:334px;padding-top:28px}

.intro{font-weight:700;font-style:italic;color:var(--green);font-size:12.6px;line-height:17px;margin-bottom:27px}
.section__title{color:var(--green);font-weight:700;font-size:14px;line-height:17px}
.section__body{color:var(--white);font-size:10.4px;line-height:14.8px;margin-bottom:9px}
.flyer--back .section__title{font-size:11.3px;line-height:14px}
.flyer--back .section__body{font-size:9.2px;line-height:14px;margin-bottom:12px}
.checklist{list-style:none;color:var(--white);font-size:9.2px;line-height:14px;margin-bottom:14px}
.checklist li::before{content:"•";margin-right:5px}

.web-band{position:absolute;left:0;width:100%;background:var(--green);color:var(--white);font-weight:700;font-size:17.5px;padding-left:28px}
.flyer--front .web-band{top:478px;height:49px;line-height:47px}

.overleaf{position:absolute;right:10px;top:568px;display:flex;align-items:center;gap:6px;font-weight:700;font-size:12.6px;color:var(--black)}
.overleaf__btn{width:23px;height:23px;border-radius:50%;background:var(--green);display:flex;align-items:center;justify-content:center}

.contact{position:absolute;left:0;top:478px;width:100%;height:155px;background:var(--green);padding:16px 28px 0}
.contact__name{font-weight:700;font-size:10.4px;line-height:12.8px;color:var(--black)}
.contact__line{font-size:10.4px;line-height:12.8px;color:var(--ink)}
.contact__web{position:absolute;left:28px;top:112px;color:var(--white);font-weight:700;font-size:17.5px}
</style>
</head>
<body>

<section class="flyer flyer--front" aria-label="Flyer front">
  <div class="brand">
    <span class="brand__dot"></span>
    <span class="brand__name">TRU Staffing</span>
  </div>
  <div class="panel">
    <p class="intro">Tru Staffing have been in the Realestate Recruitment industry for 18 years. We recruit Property Managers, Commercial and Residential, Sales and Support Staff for our clients.</p>
    <h2 class="section__title">Why clients use TRU</h2>
    <p class="section__body">With extensive years of recruitment experience we are the highest referred recruitment company in the Brisbane market. Our clients benefit from our wealth of experience and knowledge within their industry to recruit the right candidate.</p>
    <h2 class="section__title">Why candidates use TRU</h2>
    <p class="section__body">With our long standing experience within recruitment, we take the time and care attitude to find the right position and culture to suit your working experience.</p>
  </div>
  <div class="web-band">www.trustaffing.com.au</div>
  <div class="overleaf">
    <span>Tru overleaf to read more</span>
    <span class="overleaf__btn">
      <svg width="9" height="10" viewBox="0 0 9 10"><path d="M2 1 L7 5 L2 9" fill="none" stroke="#000" stroke-width="1.8"/></svg>
    </span>
  </div>
</section>

<section class="flyer flyer--back" aria-label="Flyer back">
  <div class="brand">
    <span class="brand__dot"></span>
    <span class="brand__name">TRU Staffing</span>
  </div>
  <div class="panel">
    <h2 class="section__title">Why TRU does quality and background checks on candidates</h2>
    <p class="section__body">Essed ut earum sitae ratisin nonsequi occus. Udaepratus. It prae consecte conserro int hicipsant acea sim faccae nos quatus et faccus, omnitas aspelis ciminiet, nonseditia prorentin rae vel et ea perferum eveles enis nisquiaes a vel inullatque verepel isimolu ptaepel eceaquam.</p>
    <h2 class="section__title">The advantages of using TRU Staffing vs Recruitment on your own</h2>
    <ul class="checklist">
      <li>Sed et es accus a diam quidi cum et.</li>
      <li>Omnimpedi cuptati orenit, alitae pereptate sinimos.</li>
      <li>Pro test iusda volorae poriandanda.</li>
    </ul>
    <h2 class="section__title">12 Week Guarantee period on all placements</h2>
    <p class="section__body">Untet autem volum eos eturepta doluptatem recaerum evellore arior re nobitat ilicipid molorro vidipsam harchil luptat as debit, inctate vent, si aut maximoloriam in reic temque nihil ipienti nihiciis de officto rporem.</p>
  </div>
  <div class="contact">
    <p class="contact__name">Leon Ashford, Recruitment Manager</p>
    <p class="contact__line">Mobile: 0412 583 216</p>
    <p class="contact__line">Telephone: 3715 2649</p>
    <p class="contact__line">Fax: 3715 2687</p>
    <p class="contact__line">Email: leon@trustaffing.com.au</p>
    <p class="contact__line">Level 1/ 142 Harlow Street, Fernvale QLD 4306</p>
    <p class="contact__web">www.trustaffing.com.au</p>
  </div>
</section>

</body>
</html>
```